Business card for a Exhibition booth fabrication company

Hi. My company would like to change our corporate name card. We are an events and Exhibition stand builder company. We would like our corporate name card to resonate what we do. I need someone to create something unique that relates to the industry that I am in. The graphic designer should be creative to incorporate the elements of my industry and try to blend in well in the design of the card. Our aim is to ensure that we are unique and our card can look different from our competitors.
Updates

The decision maker was very busy and didnt had time to make this decision

Target Market(s)

Marketing and events manager from all companies

Contact Information for Business Card

The business card should have the following details:
Name
Job Title
Email
Website

Colors

Designer to choose colors to be used in the design.

Requirements
Must have
• The card must be look something that is relevant to the service that I am providing. My website is: www.velmora-buildworks.example
• You can see my website to get more information on what service that I am doing
Nice to have
• On the back of my card, I would like to have a globe image with the incorporation of my company logo. This is to indicate that my services can be done in any part of the world.

```html
<!DOCTYPE html>
<html lang="en">
<head>
<meta charset="utf-8">
<title>Velmora Buildworks – Business Card</title>
<link href="https://fonts.googleapis.com/css2?family=Montserrat:wght@400;500;600;700&display=swap" rel="stylesheet">
<style>
  :root{
    --backdrop:#2b2b2e;
    --navy-deep:#13286b;
    --navy:#1d3a8f;
    --navy-light:#2c4fae;
    --accent-red:#e8232a;
    --ink-white:#ffffff;
    --ink-soft:#d9e1f5;
    --social-blue:#1e88d6;
  }
  *{box-sizing:border-box;margin:0;padding:0}
  html,body{width:1200px;height:900px;overflow:hidden}
  body{
    background:var(--backdrop);
    font-family:"Montserrat",Arial,sans-serif;
    display:flex;flex-direction:column;align-items:center;justify-content:center;gap:40px;
  }
  .card{
    position:relative;width:700px;height:400px;border-radius:22px;overflow:hidden;
    color:var(--ink-white);
    box-shadow:0 14px 30px rgba(0,0,0,.45);
  }
  .brand-mark{
    display:inline-flex;align-items:center;gap:12px;white-space:nowrap;
    font-weight:700;letter-spacing:3px;color:var(--ink-white);
  }
  .brand-dot{flex:0 0 auto;width:14px;height:14px;border-radius:50%;background:var(--accent-red)}

  /* front */
  .card-front{
    background:radial-gradient(ellipse at 50% 40%,var(--navy-light) 0%,var(--navy) 55%,var(--navy-deep) 100%);
  }
  .world-map{
    position:absolute;left:60px;top:24px;width:580px;height:230px;border-radius:40%;
    background:radial-gradient(ellipse at center,rgba(120,150,230,.45) 0%,rgba(95,127,214,.18) 55%,rgba(95,127,214,0) 75%);
  }
  .front-brand{position:absolute;left:0;right:0;top:140px;text-align:center}
  .front-brand .brand-mark{font-size:30px}
  .services{position:absolute;left:40px;right:40px;top:226px;text-align:center}
  .services-title{color:var(--accent-red);font-weight:600;font-size:15px;letter-spacing:1px;margin-bottom:10px}
  .services-list{font-size:12.5px;line-height:1.75;color:var(--ink-soft)}

  /* back */
  .card-back{background:var(--navy)}
  .back-surface{
    position:absolute;inset:0;
    background:linear-gradient(135deg,var(--navy-light) 0%,var(--navy) 45%,var(--navy-deep) 100%);
  }
  .back-brand{position:absolute;left:24px;top:188px;width:320px;text-align:center}
  .back-brand .brand-mark{font-size:20px;letter-spacing:2px;gap:10px}
  .divider{position:absolute;left:360px;top:40px;width:3px;height:320px;background:var(--accent-red)}
  .contact{position:absolute;left:392px;top:44px;right:24px}
  .person-name{font-size:30px;font-weight:500;line-height:1.1}
  .person-name strong{font-weight:700}
  .person-title{color:var(--accent-red);font-size:15px;margin:4px 0 20px}
  .contact-row{display:flex;align-items:flex-start;gap:12px;font-size:13.5px;line-height:1.4;margin-bottom:12px}
  .contact-row svg{flex:0 0 20px;width:20px;height:20px;margin-top:1px}
  .social-square{flex:0 0 20px;width:20px;height:20px;background:var(--social-blue);border-radius:2px}
</style>
</head>
<body>

<section class="card card-front">
  <div class="world-map" role="img" aria-label="World map with glowing network connections"></div>
  <div class="front-brand">
    <span class="brand-mark"><span class="brand-dot"></span>VELMORA BUILDWORKS</span>
  </div>
  <div class="services">
    <p class="services-title">OUR SERVICES</p>
    <p class="services-list">
      Exhibition Booth Fabrication | Outdoor Booth Setup | Interior Design | Installation and Dismantle<br>
      Exhibition Management | Shell Scheme Display Booth | Custom Stand Design<br>
      Exhibition Furniture and Equipment | Events Management
    </p>
  </div>
</section>

<section class="card card-back">
  <div class="back-surface" role="img" aria-label="Faceted geometric background in navy tones"></div>

  <div class="back-brand">
    <span class="brand-mark"><span class="brand-dot"></span>VELMORA BUILDWORKS</span>
  </div>

  <div class="divider"></div>

  <div class="contact">
    <h1 class="person-name">Idris <strong>Kamal</strong></h1>
    <p class="person-title">Technical marketing manager</p>

    <div class="contact-row">
      <svg viewBox="0 0 24 24"><path d="M12 2a7 7 0 0 0-7 7c0 5 7 13 7 13s7-8 7-13a7 7 0 0 0-7-7zm0 9.5A2.5 2.5 0 1 1 12 6.5a2.5 2.5 0 0 1 0 5z" fill="var(--accent-red)"/></svg>
      <span>P.O. Box 4120 Corniche Lane<br>Doha - Qatar</span>
    </div>
    <div class="contact-row">
      <svg viewBox="0 0 24 24"><path d="M12 2a7 7 0 0 0-7 7c0 5 7 13 7 13s7-8 7-13a7 7 0 0 0-7-7zm0 9.5A2.5 2.5 0 1 1 12 6.5a2.5 2.5 0 0 1 0 5z" fill="var(--accent-red)"/></svg>
      <span>Blk 2210 Harbour Road 5 #02-118<br>Singapore 40712.</span>
    </div>
    <div class="contact-row">
      <svg viewBox="0 0 24 24" fill="none" stroke="var(--accent-red)" stroke-width="2"><circle cx="12" cy="12" r="9"/><path d="M3 12h18M12 3c3 3 3 15 0 18M12 3c-3 3-3 15 0 18"/></svg>
      <span>info@velmora-buildworks.example<br>www.velmora-buildworks.example</span>
    </div>
    <div class="contact-row">
      <svg viewBox="0 0 24 24"><path d="M6.6 10.8a15 15 0 0 0 6.6 6.6l2.2-2.2a1 1 0 0 1 1-.25 11 11 0 0 0 3.6.6 1 1 0 0 1 1 1V20a1 1 0 0 1-1 1A17 17 0 0 1 3 4a1 1 0 0 1 1-1h3.5a1 1 0 0 1 1 1c0 1.25.2 2.45.6 3.6a1 1 0 0 1-.25 1z" fill="var(--accent-red)"/></svg>
      <span>028-555-0147</span>
    </div>
    <div class="contact-row">
      <span class="social-square"></span>
      <span>velmora-buildworks</span>
    </div>
  </div>
</section>

</body>
</html>
```